Summit Basin Operators, Inc. Company Brochure

I would like someone to design a brochure that can be handed out to prospective clients. We are a full service water and wastewater operations company that provides services to Municipal Utility Districts and citys. I would like something that is catchy to the eye and reflects a company that prides itself on providing personal service to its clients. We need to revamp our website, that's next, but the website does have a description of our company and services offered. You can find that information at www.summitbasinoperators.example

```html
<!DOCTYPE html>
<html lang="en">
<head>
<meta charset="utf-8">
<title>Summit Basin Operators, Inc. – Brochure Inside Spread</title>
<link href="https://fonts.googleapis.com/css2?family=Exo+2:wght@700&family=Didact+Gothic&family=Arimo&display=swap" rel="stylesheet">
<style>
  :root{
    --page-bg:#ffffff;
    --panel-edge:#a9eef6;
    --panel-center:#f4fdff;
    --panel-stroke:#dfe6e8;
    --heading-blue:#1560cf;
    --body-ink:#1e1e1e;
    --label-grey:#444444;
  }
  html,body{margin:0;padding:0;overflow:hidden;background:var(--page-bg);}
  .spread{position:relative;width:1200px;height:1000px;overflow:hidden;}
  .panels{position:absolute;left:0;top:0;}
  .heading{
    position:absolute;margin:0;
    font-family:"Exo 2",sans-serif;font-weight:700;
    font-size:12.5px;letter-spacing:.6px;line-height:16px;
    color:var(--heading-blue);text-transform:uppercase;
  }
  .body-copy{
    position:absolute;margin:0;
    font-family:"Didact Gothic",sans-serif;
    font-size:8.4px;line-height:10.7px;color:var(--body-ink);
  }
  .district-list{list-style:none;padding:0;}
  .page-label{
    position:absolute;top:730px;width:200px;text-align:center;
    font-family:"Arimo",sans-serif;font-size:18px;color:var(--label-grey);
  }
</style>
</head>
<body>
<div class="spread">
  <svg class="panels" width="1200" height="1000" viewBox="0 0 1200 1000">
    <defs>
      <radialGradient id="panelLeftFill" cx="0.62" cy="0.62" r="0.7">
        <stop offset="0" stop-color="var(--panel-center)"/>
        <stop offset="1" stop-color="var(--panel-edge)"/>
      </radialGradient>
      <radialGradient id="panelRightFill" cx="0.38" cy="0.62" r="0.7">
        <stop offset="0" stop-color="var(--panel-center)"/>
        <stop offset="1" stop-color="var(--panel-edge)"/>
      </radialGradient>
      <linearGradient id="plantPhoto" x1="0" y1="0" x2="1" y2="1">
        <stop offset="0" stop-color="#6c7a7d"/><stop offset="1" stop-color="#2f3a3c"/>
      </linearGradient>
      <linearGradient id="aeratorPhoto" x1="0" y1="0" x2="0" y2="1">
        <stop offset="0" stop-color="#5e7a5a"/><stop offset=".55" stop-color="#a9c7a0"/><stop offset="1" stop-color="#7fd46a"/>
      </linearGradient>
      <linearGradient id="drinkingPhoto" x1="0" y1="0" x2="1" y2="1">
        <stop offset="0" stop-color="#6e9a3e"/><stop offset=".5" stop-color="#d7b597"/><stop offset="1" stop-color="#49b5e0"/>
      </linearGradient>
      <linearGradient id="workerPhoto" x1="0" y1="0" x2="0" y2="1">
        <stop offset="0" stop-color="#5b9ad6"/><stop offset=".5" stop-color="#8d8a74"/><stop offset="1" stop-color="#5a6650"/>
      </linearGradient>
    </defs>

    <path class="panel panel-left" fill="url(#panelLeftFill)" stroke="var(--panel-stroke)"
      d="M600,483 A235,235 0 0 0 365,248 A235,235 0 0 0 130,483 A235,235 0 0 0 365,718 L600,718 Z"/>
    <path class="panel panel-right" fill="url(#panelRightFill)" stroke="var(--panel-stroke)"
      d="M600,718 L600,483 A235,235 0 0 1 835,248 A235,235 0 0 1 1070,483 A235,235 0 0 1 835,718 Z"/>

    <path class="photo photo-treatment-plant" role="img" aria-label="Aerial view of circular water treatment clarifiers"
      fill="url(#plantPhoto)" d="M366,545 L366,605 A60,60 0 1 1 306,545 Z"/>
    <path class="photo photo-aerator" role="img" aria-label="Green floating aerator spraying water in a treatment pond"
      fill="url(#aeratorPhoto)" d="M375,505 L469,505 A93,93 0 1 1 375,598 Z"/>
    <path class="photo photo-drinking-water" role="img" aria-label="Child drinking from a clear water bottle outdoors"
      fill="url(#drinkingPhoto)" d="M830,540 L830,449 A91,91 0 1 1 921,540 Z"/>
    <path class="photo photo-field-operator" role="img" aria-label="Operator in hard hat and safety vest taking notes at a treatment plant"
      fill="url(#workerPhoto)" d="M830,548 L897,548 A67,67 0 1 1 830,615 Z"/>
  </svg>

  <h2 class="heading" style="left:211px;top:350px;">About Our Company</h2>
  <p class="body-copy" style="left:211px;top:369px;width:156px;">Summit Basin Operators, Inc. was incorporated in the state of Texas in 1989 and is a leading competitor in the water and waste water operations industry. We are a "full service" operations company that handles all aspects of operations in the water/ wastewater industry. All personnel employed by Summit Basin Operators, Inc. are licensed by the TCEQ in water and waste water operations and obtain the proper training needed to successfully operate treatment plants to their</p>
  <p class="body-copy" style="left:373px;top:369px;width:150px;">certified to operate surface water, ground water and wastewater treatment facilities.<br>Here at Summit Basin Operators, Inc. we feel that it is important to provide the highest caliber of services available to the Districts in which we operate. We offer the ability to tailor our services based on the current needs of the District.</p>

  <h2 class="heading" style="left:676px;top:350px;">Our Mission</h2>
  <p class="body-copy" style="left:676px;top:369px;width:150px;">Summit Basin Operators, Inc.'s mission is to produce and deliver portable drinking water and treat residential wastewater in a safe, reliable, efficient and environmentally sound manner. Our vision is to be the recognized performance leader of the water and wastewater utility industry. Being a performance leader means we will achieve operational excellence, industry-leading customer satisfaction and superior financial performance.</p>

  <h2 class="heading" style="left:673px;top:563px;">Districts<br>Currently Served</h2>
  <ul class="body-copy district-list" style="left:676px;top:598px;width:140px;">
    <li>Harbor Ridge MUD</li>
    <li>Cedar Orchard</li>
    <li>Mesa Lane</li>
    <li>Kingsford</li>
    <li>Marlowe</li>
  </ul>

  <div class="page-label" style="left:293px;">Inside Page</div>
  <div class="page-label" style="left:662px;">Inside Page</div>
</div>
</body>
</html>
```